Billboard design for retail kitchen cabinet business

We have a large 7,000 square-foot showroom of beautiful kitchen cabinet displays of all different designs and price ranges. In business for over 50 years with expert designers.
Full size Halvard Media 14' X 48' billboard
Target Market(s)
Retail public on high traffic Los Angeles streets

```html
<!DOCTYPE html>
<html lang="en">
<head>
<meta charset="utf-8">
<title>Hearthline Cabinetry Billboard</title>
<link href="https://fonts.googleapis.com/css2?family=Merriweather:wght@700;900&family=Oswald:wght@600&display=swap" rel="stylesheet">
<style>
  :root {
    --page: #e9e9e9;
    --paper: #ffffff;
    --olive: #5f5540;
    --ink: #1f1f1f;
    --photo-warm: #b89a7a;
    --photo-light: #eee9e2;
    --photo-wood: #7a4a2a;
  }
  html, body { margin: 0; padding: 0; width: 1200px; height: 840px; overflow: hidden; background: var(--page); }
  .billboard {
    position: absolute; left: 30px; top: 245px; width: 1140px; height: 349px;
    background: var(--paper); overflow: hidden;
    font-family: 'Merriweather', Georgia, serif;
  }
  .headline { position: absolute; margin: 0; font-weight: 900; line-height: 1; white-space: nowrap; }
  .headline--beautifying { left: 52px; top: 42px; font-size: 60px; color: var(--olive); }
  .headline--kitchens { left: 200px; top: 102px; font-size: 60px; color: var(--olive); }
  .headline--over { left: 52px; top: 130px; font-size: 27px; font-weight: 700; color: var(--olive); }
  .headline--years { left: 52px; top: 162px; font-size: 56px; color: var(--ink); }
  .showroom-band { position: absolute; left: 0; top: 229px; width: 790px; height: 51px; }
  .showroom-text {
    position: absolute; left: 53px; top: 226px; margin: 0; height: 56px;
    display: flex; align-items: center; gap: 10px; color: #fff; font-weight: 700; font-size: 28px; white-space: nowrap;
  }
  .showroom-text .figure { font-size: 42px; font-weight: 900; }
  .contacts { position: absolute; left: 53px; top: 292px; display: flex; gap: 26px; align-items: center; }
  .contact { display: flex; align-items: center; gap: 10px; font-family: 'Oswald', 'Arial Narrow', sans-serif; font-weight: 600; font-size: 26px; color: var(--ink); }
  .contact svg { width: 33px; height: 33px; }
  .brand { position: absolute; left: 560px; top: 103px; display: flex; align-items: center; gap: 10px; }
  .brand-square { width: 22px; height: 22px; background: var(--ink); }
  .brand-name { font-weight: 900; font-size: 24px; line-height: 1.1; color: var(--ink); text-transform: uppercase; }
  .photo-collage { position: absolute; left: 0; top: 0; }
</style>
</head>
<body>
<div class="billboard">
  <svg class="photo-collage" width="1140" height="349" viewBox="0 0 1140 349">
    <defs>
      <linearGradient id="kitchenTones" x1="0" y1="0" x2="1" y2="1">
        <stop offset="0" stop-color="var(--photo-warm)"/>
        <stop offset="0.45" stop-color="var(--photo-light)"/>
        <stop offset="1" stop-color="var(--photo-wood)"/>
      </linearGradient>
    </defs>
    <polygon role="img" aria-label="Photographs of finished showroom kitchens with white and wood cabinets"
      points="790,0 1140,0 1140,349 735,349 648,253 745,155" fill="url(#kitchenTones)"/>
    <g fill="none" stroke="#fff" stroke-width="1.5">
      <polyline points="860,0 745,100 790,150"/>
      <polyline points="660,252 790,120 920,250 825,349"/>
      <polyline points="880,349 990,210 1100,330"/>
      <line x1="1140" y1="110" x2="1065" y2="180"/>
    </g>
  </svg>
  <svg class="showroom-band" viewBox="0 0 790 51" preserveAspectRatio="none" aria-hidden="true">
    <polygon points="11,0 662,0 700,0 662,51 11,51" fill="var(--olive)"/>
  </svg>

  <h1 class="headline headline--beautifying">Beautifying</h1>
  <p class="headline headline--over">for Over</p>
  <p class="headline headline--kitchens">Kitchens</p>
  <p class="headline headline--years">50 Years</p>

  <div class="brand">
    <span class="brand-square"></span>
    <span class="brand-name">Hearthline<br>Cabinetry</span>
  </div>

  <p class="showroom-text">large <span class="figure">7,000</span> square-foot showroom</p>

  <div class="contacts">
    <span class="contact">
      <svg viewBox="0 0 34 34" aria-hidden="true"><circle cx="17" cy="17" r="16" fill="var(--ink)"/><circle cx="17" cy="17" r="10" fill="var(--olive)"/><g fill="none" stroke="#fff" stroke-width="1.4"><circle cx="17" cy="17" r="8"/><ellipse cx="17" cy="17" rx="3.5" ry="8"/><line x1="9" y1="17" x2="25" y2="17"/></g></svg>
      www.hearthlinecabinetry.com
    </span>
    <span class="contact">
      <svg viewBox="0 0 34 34" aria-hidden="true"><circle cx="17" cy="17" r="16" fill="var(--ink)"/><circle cx="17" cy="17" r="10" fill="var(--olive)"/><path d="M13 10l3 0 1 4-2 1.5c1 2 2.5 3.5 4.5 4.5l1.5-2 4 1 0 3c-7 1-13-5-12-12z" fill="#fff"/></svg>
      (310) 555-0142
    </span>
  </div>
</div>
</body>
</html>
```